Simple, High-Class Web Design Wanted - Motivational Speakers Site

1. Full Brief/Request & Specs outlined on following video -
http://clipvane-recorder.com/watch/tbWrkLmQyP

2. Use colours, images as you feel suits objective (we are happy to pay up to US$30 for any good images but must have licence/permission).

3. Layout probably similar to existing site - www.podiumvoicehub.com.au / http://podiumvoicehub.com.au/contact.php

4. Must Be Able to Coded for MOBILE-FRIENDLINESS & WordPress friendly Ideal.

5. This is the first, small job of many we/graphic design jobs. If suits, winning designer may be offered all future work direct.

Thanks & look forward to your design. Glen.

Target Market(s)

corporates - high end

Number of Pages Required

2 page

Font styles to use
Sans Serif

Requirements
Must have
• Classy professional look
Nice to have
• all in Video in brief
Should not have
• too many images / new images I haven't approved

```html
<!DOCTYPE html>
<html lang="en">
<head>
<meta charset="utf-8">
<title>Free Guest &amp; Conference Speaker Recommendations</title>
<link rel="stylesheet" href="https://fonts.googleapis.com/css2?family=Oswald:wght@500;700&family=Arimo:wght@400;700&display=swap">
<style>
:root{
  --teal:#3e9fb4;
  --teal-dark:#1f6f83;
  --ink:#1d2b36;
  --blue:#1f6fb8;
  --red:#b8262b;
  --red-dark:#9c1f24;
  --navy:#1c2740;
  --text:#444;
  --note-bg:#ececec;
  --line:#d7d7d7;
  --white:#fff;
}
*{box-sizing:border-box;margin:0;padding:0}
html,body{width:744px;height:1200px;overflow:hidden;background:var(--white)}
body{font-family:"Arimo",Arial,sans-serif;color:var(--text);position:relative}
.hero-band{position:absolute;left:0;top:0;width:744px;height:140px;background:linear-gradient(180deg,#5fb7c9 0%,var(--teal) 60%,var(--teal-dark) 100%)}
.hero-title{position:absolute;left:26px;top:4px;font-family:"Oswald",Impact,sans-serif;text-transform:uppercase;line-height:1}
.hero-title .big{display:block;font-size:76px;line-height:72px;font-weight:700;color:var(--white);letter-spacing:1px}
.hero-title .amp{display:block;font-size:34px;line-height:32px;font-weight:700;color:var(--ink);margin-left:6px}
.hero-title .sub{display:block;font-size:26px;line-height:30px;font-weight:700;color:var(--ink);letter-spacing:.3px}
.speaker-art{position:absolute;right:30px;top:12px;width:96px;height:122px;border-radius:4px;background:linear-gradient(180deg,#2b6e80,#16495a)}
.contact-bar{position:absolute;left:0;top:140px;width:744px;height:30px;border-bottom:1px solid var(--line);display:flex;align-items:center;justify-content:space-between;padding:0 28px;font-size:12px}
.contact-bar .item{display:flex;align-items:center;gap:7px;color:var(--text)}
.contact-bar .phone{font-weight:700;font-size:15px;color:var(--ink)}
.headline{position:absolute;left:60px;top:180px;width:624px;text-align:center;color:var(--blue);font-size:19px;font-weight:400;line-height:25px}
.video-frame{position:absolute;left:210px;top:240px;width:324px;height:262px;background:#111;border-radius:4px;padding:10px}
.video-frame .still{width:100%;height:100%;background:linear-gradient(180deg,#f2f2f2,#c9ccd0)}
.cta-red{position:absolute;left:170px;top:515px;width:404px;height:36px;background:linear-gradient(180deg,var(--red),var(--red-dark));color:var(--white);font-family:"Oswald",Impact,sans-serif;font-weight:500;font-size:20px;letter-spacing:.4px;white-space:nowrap;display:flex;align-items:center;justify-content:center;border-radius:2px}
.intro{position:absolute;left:86px;top:568px;width:572px;font-size:10.5px;line-height:14px}
.intro a{color:var(--blue);text-decoration:none}
.checklist{position:absolute;left:120px;top:672px;list-style:none;font-size:10.5px;line-height:21px;color:var(--red)}
.checklist li{display:flex;align-items:center;gap:9px}
.outro{position:absolute;left:86px;top:762px;width:572px;font-size:10.5px;line-height:14px}
.note{position:absolute;left:86px;top:800px;width:572px;height:178px;background:var(--note-bg);border:1px solid var(--line);padding:12px 16px;font-size:10px;line-height:13.5px}
.note h3{color:var(--red);font-size:14px;font-weight:400;margin-bottom:8px;padding-bottom:6px;border-bottom:1px solid var(--line)}
.note p{margin-bottom:9px}
.cta-navy{position:absolute;left:260px;top:1014px;width:224px;height:38px;background:var(--navy);color:var(--white);font-size:15px;display:flex;align-items:center;justify-content:center;border-radius:4px}
.footer{position:absolute;left:0;top:1078px;width:744px;height:122px;background:var(--red);color:var(--white);text-align:center;font-size:10px;line-height:15px;padding-top:26px}
</style>
</head>
<body>
<header>
  <div class="hero-band"></div>
  <h1 class="hero-title"><span class="big">Free Guest</span><span class="amp">&amp;</span><span class="sub">Conference Speaker Recommendations</span></h1>
  <div class="speaker-art" role="img" aria-label="Illustration of a speaker at a podium"></div>
  <div class="contact-bar">
    <div class="item">
      <svg width="16" height="12" viewBox="0 0 16 12"><rect x="0.5" y="0.5" width="15" height="11" fill="none" stroke="#1d2b36"/><path d="M1 1l7 6 7-6" fill="none" stroke="#1d2b36"/></svg>
      suggestions@podiumvoicehub.com.au
    </div>
    <div class="item phone">
      <svg width="16" height="16" viewBox="0 0 16 16"><path d="M4 1l2.5 3-1.5 2c1 2 3 4 5 5l2-1.5 3 2.5-1.5 3C7 15 1 9 1 2.5z" fill="#1f6f83"/></svg>
      1300 48 21 67
    </div>
  </div>
</header>
<main>
  <h2 class="headline">Are you looking for a Guest or Keynote Speaker - Inspiring, Entertaining, Industry Expert etc,for a conference or special event?</h2>
  <div class="video-frame"><div class="still" role="img" aria-label="Video still of the presenter speaking to camera"></div></div>
  <div class="cta-red">I want to Make our Event a Great Success</div>
  <p class="intro">Podium Voice Hub is a <a href="#">free industry service</a> designed to help people looking for speakers save precious time and frustration in finding the most suitable/best speaker for their needs.<br>Suggestions are given by Australian conference speaker Glen Carver, who has presented around Australia for a number of years and is familiar with many of our top professional speakers, MC's as well as the leading speaker bureaus.<br>If you would like a hand finding some good speaker options, simply send us the details of your event and the type of presenter you are ideally after, e.g.</p>
  <ul class="checklist">
    <li><svg width="12" height="10" viewBox="0 0 12 10"><path d="M1 5l3.5 3.5L11 1" fill="none" stroke="#3a8a3a" stroke-width="2"/></svg>Type/Style – Motivational, Entertaining, Keynote/Workshop, MC etc</li>
    <li><svg width="12" height="10" viewBox="0 0 12 10"><path d="M1 5l3.5 3.5L11 1" fill="none" stroke="#3a8a3a" stroke-width="2"/></svg>Topic/Area - Team Building, Leadership, Inspiration, Health/Life Balance etc</li>
    <li><svg width="12" height="10" viewBox="0 0 12 10"><path d="M1 5l3.5 3.5L11 1" fill="none" stroke="#3a8a3a" stroke-width="2"/></svg>Approximate Budget - $1000, $2500, $5000, $7500+ etc</li>
    <li><svg width="12" height="10" viewBox="0 0 12 10"><path d="M1 5l3.5 3.5L11 1" fill="none" stroke="#3a8a3a" stroke-width="2"/></svg>Location - Sydney, Melbourne, Brisbane, Perth, Adelaide, Canberra etc</li>
  </ul>
  <p class="outro">and where we can, we will be happy to send you some speaker possibilities/ideas, trusted speakers bureaus or simply some thoughts on the best places for you to look. Regards PVH.</p>
  <section class="note">
    <h3>Please Note:</h3>
    <p>Any information you provide will ONLY ever be used to help with your specific enquiry.</p>
    <p>Glen does not have any financial agreements with any individual speakers he recommends. He offers this service, as it only takes a few minutes of his time, helps promote other professional speakers and obviously keeps his own name out there in the industry.</p>
    <p>Please understand that while Glen tries to respond quickly, due to his own speaking/travel commitments it may take up to 24 hours.</p>
  </section>
  <div class="cta-navy">Quick Online Contact Form »</div>
</main>
<footer class="footer">
  © 2013. All Rights Reserved www.podiumvoicehub.com.au PO Box 412 Harbour Point NSW 2071<br>
  E: suggestions@podiumvoicehub.com.au Phone: 1300 48 21 67
</footer>
</body>
</html>
```